Nobody Left the Lantern Burning - Tom Halvery - CD Cover Design Project

Single Cover for CD & Online media e.g. Tunebox Graphics
The first song release from Tom Halvery will be the track 'Nobody Left the Lantern Burning'.
For the release the single requires artwork that is eye catching, seriously professional & meets the requirements of Disc Sprout, Tunebox and also a physical copy on CD.
Track listings for CD will be:
1. Nobody Left the Lantern Burning
2. Nobody Left the Lantern Burning - Instrumental
see details in this link:
http://members.discsprout-example.com/faq.aspx
http://selfmadesound.discsprout-example.com/2009/11/avoid-album-art-atrocities/
http://answers.quorvex-example.com/question/index?qid=20111015141433AAdDTmH
Any advice on this would be greatly appreciated,
I would also like the two logo's I have uploaded to be used,
one is the Tom Halvery logo and the other is for Milbrook & Tandy Records logo (please remove the R and replace with a C for copyright.)
There are four high res photo shopped pictures of Tom Halvery and another zip file of many others, it would be nice to include one of these maybe on the 2nd page or back of the CD. Please don't use them as the front cover.
I imagine an Art Deco illustration but please listen to the track and let it inspire you.
Good Luck
Updates
I don't feel this is what I'm looking for, the design needs to refelct a broken heart without being a picture of a broken heart
Reason: No design has been what we are after so far so the deadline has been extended and the budget increased.

```html
<!DOCTYPE html>
<html lang="en">
<head>
<meta charset="utf-8">
<title>Nobody Left the Lantern Burning — Tom Halvery</title>
<link href="https://fonts.googleapis.com/css2?family=Oswald:wght@400;600&display=swap" rel="stylesheet">
<style>
  :root {
    --paint-red: #f0241a;
    --paint-orange: #f4521f;
    --paint-pink: #e98bb8;
    --paint-violet: #3b1d55;
    --ink-white: #ffffff;
    --ink-black: #111111;
    --label-maroon: #6e1f2e;
  }
  html, body {
    margin: 0;
    padding: 0;
    width: 1200px;
    height: 1200px;
    overflow: hidden;
    background: #ffffff;
  }
  .cover {
    position: relative;
    width: 1200px;
    height: 1200px;
    overflow: hidden;
    font-family: "Oswald", "Arial Narrow", sans-serif;
  }
  .cover-artwork {
    position: absolute;
    inset: 0;
    background:
      radial-gradient(ellipse 70% 28% at 62% 86%, var(--paint-violet) 0%, rgba(59,29,85,0.85) 45%, rgba(59,29,85,0) 75%),
      linear-gradient(170deg, var(--paint-pink) 0%, var(--paint-red) 22%, var(--paint-orange) 50%, var(--paint-red) 75%, #b51a2a 100%);
  }
  .title {
    position: absolute;
    left: 381px;
    top: 408px;
    margin: 0;
    color: var(--ink-white);
    font-weight: 400;
    letter-spacing: -2px;
    line-height: 1;
  }
  .title-line {
    display: block;
  }
  .title-line--first,
  .title-line--second {
    font-size: 150px;
    line-height: 128px;
  }
  .title-line--third {
    font-size: 112px;
    line-height: 104px;
  }
  .artist-mark {
    position: absolute;
    right: 130px;
    top: 52px;
    display: flex;
    flex-direction: column;
    align-items: center;
    gap: 10px;
    color: var(--ink-black);
    font-weight: 600;
    text-transform: uppercase;
    line-height: 0.95;
    text-align: center;
  }
  .artist-mark-square {
    width: 96px;
    height: 96px;
    background: var(--ink-black);
  }
  .artist-mark-name {
    font-size: 34px;
  }
  .label-mark {
    position: absolute;
    left: 48px;
    bottom: 56px;
    display: flex;
    flex-direction: column;
    align-items: center;
    gap: 12px;
    color: var(--label-maroon);
    font-weight: 600;
  }
  .label-mark-circle {
    width: 88px;
    height: 88px;
    border-radius: 50%;
    background: var(--label-maroon);
  }
  .label-mark-name {
    font-size: 20px;
    text-transform: uppercase;
    letter-spacing: 0.5px;
  }
</style>
</head>
<body>
  <main class="cover">
    <div class="cover-artwork" role="img" aria-label="Abstract painted background in red, orange and pink brush strokes with a white blade shape and large dark violet lips across the lower half"></div>

    <h1 class="title">
      <span class="title-line title-line--first">Nobody</span>
      <span class="title-line title-line--second">Left the</span>
      <span class="title-line title-line--third">Lantern Burning</span>
    </h1>

    <div class="artist-mark">
      <span class="artist-mark-square"></span>
      <span class="artist-mark-name">Tom<br>Halvery</span>
    </div>

    <div class="label-mark">
      <span class="label-mark-circle"></span>
      <span class="label-mark-name">Milbrook &amp; Tandy Records</span>
    </div>
  </main>
</body>
</html>
```